Label for kLw Homestead beef tallow

I need a small label to go on a 2oz amber glass jar as well as a 4 oz. amber glass jar of moisturizer.
I prefer it to be rectangular for the 2oz jar since it's small and square for the 4oz jar.
I'd like to keep our kLw Homestead logo the same font and style, which is attached. Ten Sleep, Wyoming should be left out. The font for kLw Homestead is spartan.
The label content is as follows:
Meadow Tallow
Whipped Moisturizer
Ingredients: Beef Tallow, jojoba oil, peppermint oil.
2oz. jar

Instead of a white label, I'm thinking of a tan or brown label that will blend in with the amber jar. The lettering could then be a white, cream or even rust/burgandy color. Something to give it a rich look.

Thank you!

Target Market(s)

Mainly women but men as well.

Industry/Entity Type

Ranching and online beef sales

Requirements
Must have
• kLw Homestead logo

```html
<!DOCTYPE html>
<html lang="en">
<head>
<meta charset="utf-8">
<title>kLw Homestead – Meadow Tallow Labels</title>
<link rel="stylesheet" href="https://fonts.googleapis.com/css2?family=League+Spartan:wght@400&family=Great+Vibes&family=Josefin+Sans:wght@300;400&display=swap">
<style>
  :root {
    --page-bg: #ecebe8;
    --label-gold: #b98a2e;
    --label-pearl: #e9e9ea;
    --label-wine: #722a45;
    --oval-white: #ffffff;
    --ink-black: #1a1a1a;
    --ink-wine: #7a2a4a;
    --ink-gold: #c79a3a;
    --ink-grey: #3a3a3a;
  }
  * { box-sizing: border-box; margin: 0; padding: 0; }
  html, body {
    width: 1200px;
    height: 800px;
    overflow: hidden;
    background: var(--page-bg);
  }
  .label-sheet {
    width: 1200px;
    height: 800px;
    display: flex;
    flex-direction: column;
    align-items: center;
    justify-content: center;
    gap: 30px;
  }
  .jar-label {
    width: 560px;
    height: 220px;
    display: flex;
    align-items: center;
    justify-content: center;
  }
  .jar-label--gold { background: var(--label-gold); }
  .jar-label--pearl { background: var(--label-pearl); }
  .jar-label--wine { background: var(--label-wine); }

  .label-oval {
    width: 440px;
    height: 204px;
    border-radius: 50%;
    background: var(--oval-white);
    display: flex;
    flex-direction: column;
    align-items: center;
    justify-content: center;
    text-align: center;
    padding-top: 4px;
  }
  .brand-name {
    font-family: "League Spartan", sans-serif;
    font-weight: 400;
    font-size: 38px;
    letter-spacing: 1px;
    color: var(--ink-black);
    line-height: 1;
  }
  .product-name {
    font-family: "Great Vibes", cursive;
    font-size: 38px;
    line-height: 1.05;
    color: var(--ink-wine);
    margin-top: 4px;
  }
  .jar-label--wine .product-name { color: var(--ink-gold); }
  .product-type {
    font-family: "Josefin Sans", sans-serif;
    font-weight: 300;
    font-size: 16px;
    color: var(--ink-grey);
    margin-top: 2px;
  }
  .ingredients {
    font-family: "Josefin Sans", sans-serif;
    font-weight: 300;
    font-size: 12px;
    color: var(--ink-grey);
    margin-top: 3px;
  }
  .net-size {
    font-family: "Josefin Sans", sans-serif;
    font-weight: 300;
    font-size: 11px;
    color: var(--ink-grey);
    margin-top: 12px;
  }
</style>
</head>
<body>
  <main class="label-sheet">
    <section class="jar-label jar-label--gold">
      <div class="label-oval">
        <p class="brand-name">kLw Homestead</p>
        <p class="product-name">Meadow tallow</p>
        <p class="product-type">whipped moisturizer</p>
        <p class="ingredients">Ingredients: Beef Tallow, jojoba oil, peppermint oil</p>
        <p class="net-size">2oz. Jar</p>
      </div>
    </section>
    <section class="jar-label jar-label--pearl">
      <div class="label-oval">
        <p class="brand-name">kLw Homestead</p>
        <p class="product-name">Meadow tallow</p>
        <p class="product-type">whipped moisturizer</p>
        <p class="ingredients">Ingredients: Beef Tallow, jojoba oil, peppermint oil</p>
        <p class="net-size">2oz. Jar</p>
      </div>
    </section>
    <section class="jar-label jar-label--wine">
      <div class="label-oval">
        <p class="brand-name">kLw Homestead</p>
        <p class="product-name">Meadow tallow</p>
        <p class="product-type">whipped moisturizer</p>
        <p class="ingredients">Ingredients: Beef Tallow, jojoba oil, peppermint oil</p>
        <p class="net-size">2oz. Jar</p>
      </div>
    </section>
  </main>
</body>
</html>
```